Banner
Zielgruppe
Wir sind Estrichleger und Beschichter. Wir erstellen u. a. Sichtestrich und Beschichtungen im Wohnbereich und für Gewerbekunden im Industriebereich (Hallen und Tiefgaragen).
Unsere Zielgruppe sind sowohl Privatverbraucher im gehobenen Segment als auch Bauträger und Gewerbekunden
Aufgabenstellung
Gute Lesbarkeit, klare Botschaft auch wenn die Banner in großer Höhe angebracht werden.
Masse:
Bauzaunbanner aus Mesh-Plane, 340x173 cm,
wird gedruckt auf
hochwertige Mehs-Plane, rundum, umsäumt und veröst, 4/0-farbig (einseitig mit Motiv bedruck), 270 g Meshgewebe-Plane - winddurchlässig und wetterfest, (B1- zertifiziert - schwer entflammbar nach DIN 4102)
Es ist wünschenswert den Claim: 'Ich steh drauf' mit auf dem Banner zu platzieren.
Wir haben gerade die Fahrzeuge neu designen lassen, der Gewinner ist hochgeladen. Gern können Sie sich an diesem orientieren.

```html
<!DOCTYPE html>
<html lang="de">
<head>
<meta charset="utf-8">
<title>Brandt Bodentechnik – Bauzaunbanner</title>
<link rel="stylesheet" href="https://fonts.googleapis.com/css2?family=Roboto:wght@400;700&family=Caveat+Brush&display=swap">
<style>
  :root {
    --stage: #d9d9d9;
    --paper: #ffffff;
    --brand-red: #a71c24;
    --ink: #111111;
    --warm-grey: #67625c;
  }
  html, body {
    margin: 0;
    width: 1200px;
    height: 1200px;
    overflow: hidden;
    background: var(--stage);
  }
  .banner {
    position: absolute;
    left: 131.7px;
    top: 360.9px;
    width: 937.9px;
    height: 477.6px;
    display: block;
  }
  .banner__paper { fill: var(--paper); }
  .banner__frame { fill: none; stroke: var(--brand-red); stroke-width: 3; }
  .banner__band { fill: var(--brand-red); }
  .brand-name {
    font-family: "Roboto", sans-serif;
    font-weight: 400;
    fill: var(--warm-grey);
    font-size: 84px;
  }
  .claim {
    font-family: "Caveat Brush", cursive;
    fill: var(--ink);
    font-size: 150px;
  }
  .web-address {
    font-family: "Roboto", sans-serif;
    font-weight: 700;
    fill: var(--paper);
    font-size: 62px;
  }
  .phone {
    font-family: "Roboto", sans-serif;
    font-weight: 700;
    fill: var(--ink);
    font-size: 76px;
  }
  .contact {
    font-family: "Roboto", sans-serif;
    font-weight: 400;
    fill: var(--ink);
    font-size: 34px;
  }
</style>
</head>
<body>
<svg class="banner" viewBox="212 581 1510 769" xmlns="http://www.w3.org/2000/svg" aria-label="Bauzaunbanner Brandt Bodentechnik">
  <rect class="banner__paper" x="212" y="581" width="1510" height="769"/>
  <rect class="banner__frame" x="266" y="638" width="1400" height="654"/>

  <g class="brand-name">
    <text x="320" y="820">Brandt</text>
    <text x="320" y="920">Bodentechnik</text>
  </g>

  <text class="claim" x="1085" y="835" textLength="535" lengthAdjust="spacingAndGlyphs">Ich steh´drauf</text>

  <polygon class="banner__band" points="212,1068 1722,870 1722,970 212,1168"/>

  <text class="web-address" x="1638" y="960" text-anchor="end" transform="rotate(-7.47 1638 960)">brandt-bodentechnik.de</text>

  <text class="phone" x="305" y="1236" transform="rotate(-7.47 305 1236)">+49 (0) 8000/5550123</text>

  <g class="contact" text-anchor="end">
    <text x="1638" y="1106">Lukas Ferner</text>
    <text x="1638" y="1153">Lindenweg 7</text>
    <text x="1638" y="1200">83209 Musterau</text>
    <text x="1638" y="1247">info@brandt-bodentechnik.de</text>
  </g>
</svg>
</body>
</html>
```